Residential Construction Business - Site Signage

I need a design made for a site fence banner. We have a logo and branding so the design would need to be aligned with this. It would need to be made to specific size ratio so that it can be sent to the maker for production.
ratio : 4600 wide x 1700 high
The design should feature our website and also the slogan
"don't move, re-imagine"

Target Market(s)

potential clients

Industry/Entity Type

construction

Font styles to use
Other font styles liked:
• to match branding

Colors
0054AA
0677BA
7BADD7
CADEEF
E8F1F8

Requirements
Must have
• www.velmbuild.com.au Majority of the sign is our brand logo
Nice to have
• Majority of the sign is our brand logo
Should not have
• colors and themes that arent brand relevant

```html
<!DOCTYPE html>
<html lang="en">
<head>
<meta charset="utf-8">
<title>Velm Build – Site Fence Banner</title>
<link href="https://fonts.googleapis.com/css2?family=Montserrat:wght@500;600;700&display=swap" rel="stylesheet">
<style>
  :root {
    --page: #ffffff;
    --navy: #0b2547;
    --navy-deep: #061a33;
    --black: #000000;
    --white: #ffffff;
    --brand-blue: #0a5a9c;
    --accent: #1a9ad6;
    --outline: #1d3f63;
  }
  * { margin: 0; padding: 0; box-sizing: border-box; }
  html, body { width: 1200px; height: 1200px; overflow: hidden; background: var(--page); }
  body { position: relative; font-family: "Montserrat", sans-serif; }

  .banner {
    position: absolute; left: 32px; top: 398px; width: 1136px; height: 398px;
    background: radial-gradient(ellipse at 30% 40%, #123a66 0%, var(--navy) 45%, var(--navy-deep) 100%);
    overflow: hidden;
  }
  .house-photo {
    position: absolute; left: 464px; top: 220px; width: 320px; height: 178px;
    background: linear-gradient(160deg, #1a3556 0%, #2a4a66 40%, #6b6a5a 70%, #2b3b2c 100%);
    clip-path: polygon(30% 0, 100% 0, 100% 100%, 0 100%);
  }
  .brand-panel { position: absolute; inset: 0; width: 100%; height: 100%; }

  .headline {
    position: absolute; left: 62px; top: 88px;
    font-weight: 600; font-size: 78px; line-height: 70px; letter-spacing: -2px;
  }
  .headline .line-1 { color: var(--white); display: block; }
  .headline .line-2 { color: var(--brand-blue); display: block; }
  .rule { position: absolute; left: 62px; top: 242px; width: 100px; height: 3px; background: var(--accent); }
  .services {
    position: absolute; left: 62px; top: 269px; color: var(--white);
    font-weight: 600; font-size: 13px; letter-spacing: 4.6px; white-space: nowrap;
  }
  .features { position: absolute; left: 62px; top: 314px; display: flex; }
  .feature { display: flex; flex-direction: column; align-items: center; color: var(--white); font-size: 7.5px; font-weight: 600; letter-spacing: 1px; text-align: center; line-height: 9px; }
  .feature svg { width: 30px; height: 30px; margin-bottom: 7px; }
  .feature--design { width: 64px; }
  .feature--craft { width: 90px; margin-left: 50px; }
  .feature--time { width: 90px; margin-left: 22px; }

  .wordmark {
    position: absolute; left: 600px; top: 170px; color: var(--white);
    font-weight: 700; font-size: 37px; letter-spacing: 13.2px; white-space: nowrap;
  }
  .web-link {
    position: absolute; left: 814px; top: 328px; width: 280px; height: 38px;
    border: 1.5px solid var(--outline); border-radius: 19px;
    display: flex; align-items: center; justify-content: center;
    color: var(--white); font-weight: 600; font-size: 15px; letter-spacing: 3px;
  }
</style>
</head>
<body>
  <div class="banner">
    <div class="house-photo" role="img" aria-label="Modern two-storey house at dusk with lit glass doors and garden path"></div>
    <svg class="brand-panel" viewBox="0 0 1136 398" aria-hidden="true">
      <path d="M736 0 H1136 V398 H776 L572 206 Q560 192 572 178 Z" fill="#000"/>
    </svg>

    <h1 class="headline"><span class="line-1">don’t move,</span><span class="line-2">re-imagine</span></h1>
    <div class="rule"></div>
    <p class="services">RENOVATE &nbsp;|&nbsp; EXTEND &nbsp;|&nbsp; TRANSFORM</p>

    <div class="features">
      <div class="feature feature--design">
        <svg viewBox="0 0 30 30" fill="none" stroke="#fff" stroke-width="1.3">
          <path d="M4 4 V26 M2 4 H6 M2 26 H6" stroke="#1a9ad6"/>
          <path d="M9 15 L18 7 L27 15 M11 13 V26 H25 V13 M15 26 V19 H20 V26"/>
          <path d="M25 3 V7 M23 5 H27"/>
        </svg>
        DESIGN-LED
      </div>
      <div class="feature feature--craft">
        <svg viewBox="0 0 30 30" fill="none" stroke="#fff" stroke-width="1.3">
          <path d="M5 21 Q5 9 15 8 Q25 9 25 21 M3 21 H27 V24 H3 Z M12 8 V15 M18 8 V15 M12 8 Q15 6 18 8"/>
        </svg>
        QUALITY<br>CRAFTSMANSHIP
      </div>
      <div class="feature feature--time">
        <svg viewBox="0 0 30 30" fill="none" stroke="#fff" stroke-width="1.3">
          <rect x="7" y="5" width="16" height="22" rx="1"/>
          <rect x="11" y="3" width="8" height="4" rx="1"/>
          <path d="M11 16 L14 19 L20 12" stroke="#1a9ad6"/>
        </svg>
        ON TIME<br>&amp; ON BUDGET
      </div>
    </div>

    <div class="wordmark">VELM BUILD</div>
    <div class="web-link">velmbuild.com.au</div>
  </div>
</body>
</html>
```